Retail Jewelry Business Card Design Project

We are in need of a new business card design for a retail jewelry store. This store is in the business of fine jewelry including but not specific to bridal jewelry, diamonds, designer jewelry and watches.

This store has been in business for 20 years but continues to strive for a modern professional appeal. The main colors use for this business are a royal blue, white and silver.

Target Market(s)

Target market is ages 18-50

Industry/Entity Type

Jewelry

Requirements
Must have
• Sales Person Name
Sales Person Email Address

Store Address
Store Phone
Website

Standard business card size. No odd shapes or sizes.
Nice to have
• Overall modern feel for card.

We have thought that a design with a nice feature of the logo on the back of the card would be nice but open to ideas.
Should not have
• No specific images of jewelry should be used.

```html
<!DOCTYPE html>
<html lang="en">
<head>
<meta charset="utf-8">
<title>Marlowe Reid Fine Jewelry – Business Card</title>
<link href="https://fonts.googleapis.com/css2?family=Source+Sans+3:wght@400;600&display=swap" rel="stylesheet">
<style>
  :root {
    --navy-deep: #0b1024;
    --navy-mid: #1a2446;
    --royal: #2f2f8e;
    --lavender: #7b70c2;
    --ink: #3f3f48;
    --paper: #ffffff;
    --stage: #ffffff;
  }
  * { margin: 0; padding: 0; box-sizing: border-box; }
  html, body {
    width: 1200px; height: 1000px; overflow: hidden;
    background: var(--stage);
    font-family: "Source Sans 3", "Helvetica Neue", Arial, sans-serif;
  }
  .canvas { position: relative; width: 1200px; height: 1000px; }

  .card {
    position: absolute; left: 287px; width: 653px; height: 372px;
    border-radius: 28px; overflow: hidden;
    box-shadow: 4px 5px 6px rgba(0,0,0,0.28);
  }
  .card--front {
    top: 103px;
    background: radial-gradient(ellipse at 35% 30%, var(--navy-mid) 0%, var(--navy-deep) 75%);
  }
  .card--back { top: 533px; background: var(--paper); }

  .brand-name {
    position: absolute; font-weight: 600; line-height: 1.05;
  }
  .card--front .brand-name {
    left: 42px; top: 212px; color: var(--paper); font-size: 44px;
  }
  .card--back .brand-name {
    left: 40px; top: 140px; color: var(--royal); font-size: 40px;
  }
  .brand-name small {
    display: block; font-size: 0.46em; letter-spacing: 0.18em;
    text-transform: uppercase; margin-top: 6px; padding-left: 44px;
  }

  .card--front .web {
    position: absolute; left: 74px; top: 320px;
    color: var(--paper); font-size: 17px; letter-spacing: 0.06em;
  }

  .contact { position: absolute; left: 361px; top: 96px; color: var(--ink); font-size: 16px; line-height: 22px; }
  .contact .person { font-size: 20px; font-weight: 600; color: var(--royal); }
  .contact .person span { color: var(--lavender); }
  .contact .title { margin-bottom: 34px; }
  .contact .address { margin-bottom: 12px; }
  .contact .line { display: flex; align-items: center; gap: 8px; }
  .contact .line svg { width: 17px; height: 14px; fill: var(--lavender); }

  .web-band { position: absolute; right: 0; bottom: 0; width: 345px; height: 34px; }
  .web-band svg { position: absolute; inset: 0; }
  .web-band p {
    position: relative; padding-left: 63px; line-height: 34px;
    color: var(--paper); font-size: 17px; letter-spacing: 0.06em;
  }
</style>
</head>
<body>
<main class="canvas">

  <section class="card card--front" aria-label="Card front">
    <h1 class="brand-name">Marlowe Reid<small>Fine Jewelry</small></h1>
    <p class="web">www.marlowereidjewelry.com</p>
  </section>

  <section class="card card--back" aria-label="Card back">
    <h2 class="brand-name">Marlowe Reid<small>Fine Jewelry</small></h2>

    <div class="contact">
      <p class="person">Marlowe Reid <span>Halden</span></p>
      <p class="title">Owner</p>
      <p class="address">2290 Linden Avenue<br>Bayport, FL 32499</p>
      <p class="line">
        <svg viewBox="0 0 17 14" aria-hidden="true"><path d="M1 5c0-3 15-3 15 0v1h-4V4H5v2H1z"/><rect x="2" y="7" width="13" height="7" rx="1"/></svg>
        000.000.0000
      </p>
      <p class="line">
        <svg viewBox="0 0 17 14" aria-hidden="true"><path d="M1 2h15v10H1z M2 3l6.5 5L15 3" /><path d="M1 2h15L8.5 8z" fill="#fff" opacity=".55"/></svg>
        marlowe@marlowereidjewelry.com
      </p>
    </div>

    <div class="web-band">
      <svg viewBox="0 0 345 34" preserveAspectRatio="none" aria-hidden="true">
        <defs>
          <linearGradient id="bandFill" x1="0" x2="1">
            <stop offset="0" stop-color="#0b1024"/>
            <stop offset="1" stop-color="#1a2446"/>
          </linearGradient>
        </defs>
        <path d="M0 34 C14 22 20 2 44 0 H345 V34 Z" fill="url(#bandFill)"/>
      </svg>
      <p>www.marlowereidjewelry.com</p>
    </div>
  </section>

</main>
</body>
</html>
```